Redesign Business Cards, Attached

Please read instructions carefully. If you have any questions send a message before submitting your ONE design. Please redesign attached business cards. Double sided. Use same content and descriptions. Use black, silver, crimson red and gold colors. My only issue with the attached design is the background colors. I like the layout as-is. I can provide the individual pictures on the back side later. Do not submit more than one design. One submission shall include both front and back. Do not submit front and back separately. A second project will be launched to create a matching post card after completion of this.
Industry/Entity Type
see description and attachments.
Contact Information for Business Card
Requirements
Must have
- see description and attachments.
Nice to have
Should not have

```html
<!DOCTYPE html>
<html lang="en">
<head>
<meta charset="utf-8">
<title>Harbor Line Boat Academy – Business Card</title>
<link rel="stylesheet" href="https://fonts.googleapis.com/css2?family=Montserrat:wght@500;600;700;800&display=swap">
<style>
  :root {
    --crimson: #9e0f12;
    --crimson-deep: #7d0a0c;
    --black: #141414;
    --gold: #e8b62c;
    --gold-light: #f7d766;
    --white: #ffffff;
    --paper: #f4f4f4;
    --canvas: #d9d6d2;
  }
  html, body {
    margin: 0;
    width: 1200px;
    height: 900px;
    overflow: hidden;
    background: var(--canvas);
    font-family: "Montserrat", Arial, sans-serif;
  }
  .card-sheet { display: block; width: 1200px; height: 900px; }
  .brand-name { font-weight: 700; fill: var(--white); font-size: 17px; }
  .brand-name.large { font-size: 21px; }
  .tile-text { font-size: 10px; font-weight: 500; }
  .tile-text.on-red { fill: var(--white); }
  .tile-text.on-white { fill: var(--black); }
  .site-line { fill: var(--white); font-size: 17px; font-weight: 500; }
  .person-name { fill: var(--gold); font-size: 23px; font-weight: 800; letter-spacing: .3px; }
  .person-role { fill: var(--white); font-size: 20px; font-weight: 600; }
  .pill-label { fill: var(--gold); font-size: 18px; font-weight: 800; }
  .pill-phone { fill: var(--white); font-size: 19px; font-weight: 700; }
  .contact-line { fill: var(--white); font-size: 15px; font-weight: 500; }
</style>
</head>
<body>
<svg class="card-sheet" viewBox="0 0 1200 900" xmlns="http://www.w3.org/2000/svg">
  <defs>
    <linearGradient id="goldFoil" x1="0" y1="0" x2="1" y2="1">
      <stop offset="0" stop-color="var(--gold-light)"/>
      <stop offset=".5" stop-color="var(--gold)"/>
      <stop offset="1" stop-color="#c9931c"/>
    </linearGradient>
    <linearGradient id="crimsonField" x1="0" y1="0" x2="1" y2="1">
      <stop offset="0" stop-color="var(--crimson)"/>
      <stop offset="1" stop-color="var(--crimson-deep)"/>
    </linearGradient>
    <linearGradient id="seaTone" x1="0" y1="0" x2="1" y2="1">
      <stop offset="0" stop-color="#8fa6bd"/>
      <stop offset=".6" stop-color="#3d5a78"/>
      <stop offset="1" stop-color="#c9d6e2"/>
    </linearGradient>
    <clipPath id="backClip"><rect width="680" height="389" rx="14"/></clipPath>
    <clipPath id="frontClip"><rect width="680" height="389" rx="14"/></clipPath>
  </defs>

  <!-- Back side -->
  <g class="card card-back" transform="translate(260 40)">
    <g clip-path="url(#backClip)">
      <rect class="field-crimson" width="680" height="389" fill="url(#crimsonField)"/>
      <rect class="band-black" y="255" width="680" height="134" fill="var(--black)"/>
      <rect class="band-black" x="452" y="236" width="228" height="30" fill="var(--black)"/>
      <rect class="band-black" x="560" y="150" width="120" height="110" fill="var(--black)"/>
      <polygon class="photo-area" role="img" aria-label="Photo of a white motor yacht cruising across open water"
               points="402,0 680,0 680,160 412,178 380,140" fill="url(#seaTone)"/>
      <polyline class="gold-edge" points="396,0 370,140 408,180" fill="none" stroke="url(#goldFoil)" stroke-width="7"/>

      <g class="brand-mark">
        <circle cx="66" cy="84" r="16" fill="var(--gold)"/>
        <text class="brand-name" x="92"><tspan y="80">Harbor Line</tspan><tspan x="92" y="100">Boat Academy</tspan></text>
      </g>

      <g class="service-grid">
        <rect x="130" y="198" width="104" height="58" fill="var(--crimson)" stroke="var(--black)" stroke-width="2"/>
        <text class="tile-text on-red" x="182" text-anchor="middle"><tspan y="214">Lorem ipsum</tspan><tspan x="182" y="226">dolor sit amet,</tspan><tspan x="182" y="238">consectetuer</tspan><tspan x="182" y="250">adipiscing elit,</tspan></text>
        <rect x="130" y="256" width="104" height="58" fill="var(--paper)" stroke="var(--black)" stroke-width="2"/>
        <text class="tile-text on-white" x="182" text-anchor="middle"><tspan y="272">Lorem ipsum</tspan><tspan x="182" y="284">dolor sit amet,</tspan><tspan x="182" y="296">consectetuer</tspan><tspan x="182" y="308">adipiscing elit,</tspan></text>

        <rect x="238" y="172" width="104" height="58" fill="var(--paper)" stroke="var(--black)" stroke-width="2"/>
        <text class="tile-text on-white" x="290" text-anchor="middle"><tspan y="188">Lorem ipsum</tspan><tspan x="290" y="200">dolor sit amet,</tspan><tspan x="290" y="212">consectetuer</tspan><tspan x="290" y="224">adipiscing elit,</tspan></text>
        <rect x="238" y="230" width="104" height="58" fill="var(--crimson)" stroke="var(--black)" stroke-width="2"/>
        <text class="tile-text on-red" x="290" text-anchor="middle"><tspan y="246">Lorem ipsum</tspan><tspan x="290" y="258">dolor sit amet,</tspan><tspan x="290" y="270">consectetuer</tspan><tspan x="290" y="282">adipiscing elit,</tspan></text>

        <rect x="346" y="146" width="104" height="58" fill="var(--crimson)" stroke="var(--black)" stroke-width="2"/>
        <text class="tile-text on-red" x="398" text-anchor="middle"><tspan y="162">Lorem ipsum</tspan><tspan x="398" y="174">dolor sit amet,</tspan><tspan x="398" y="186">consectetuer</tspan><tspan x="398" y="198">adipiscing elit,</tspan></text>
        <rect x="346" y="204" width="104" height="58" fill="var(--paper)" stroke="var(--black)" stroke-width="2"/>
        <text class="tile-text on-white" x="398" text-anchor="middle"><tspan y="220">Lorem ipsum</tspan><tspan x="398" y="232">dolor sit amet,</tspan><tspan x="398" y="244">consectetuer</tspan><tspan x="398" y="256">adipiscing elit,</tspan></text>

        <rect x="454" y="120" width="104" height="58" fill="var(--paper)" stroke="var(--black)" stroke-width="2"/>
        <text class="tile-text on-white" x="506" text-anchor="middle"><tspan y="136">Lorem ipsum</tspan><tspan x="506" y="148">dolor sit amet,</tspan><tspan x="506" y="160">consectetuer</tspan><tspan x="506" y="172">adipiscing elit,</tspan></text>
        <rect x="454" y="178" width="104" height="58" fill="var(--crimson)" stroke="var(--black)" stroke-width="2"/>
        <text class="tile-text on-red" x="506" text-anchor="middle"><tspan y="194">Lorem ipsum</tspan><tspan x="506" y="206">dolor sit amet,</tspan><tspan x="506" y="218">consectetuer</tspan><tspan x="506" y="230">adipiscing elit,</tspan></text>
      </g>

      <text class="site-line" x="400" y="352" text-anchor="middle">www.HelmReady.com</text>
    </g>
  </g>

  <!-- Front side -->
  <g class="card card-front" transform="translate(260 470)">
    <g clip-path="url(#frontClip)">
      <rect class="field-crimson" width="680" height="389" fill="url(#crimsonField)"/>
      <polygon class="gold-chevron" points="300,0 356,0 340,150 322,232 500,389 440,389 282,232 296,150" fill="url(#goldFoil)"/>
      <polygon class="field-black" points="362,0 680,0 680,389 508,389 332,232 350,150" fill="var(--black)"/>

      <g class="brand-mark">
        <circle cx="62" cy="204" r="18" fill="var(--gold)"/>
        <text class="brand-name large" x="92"><tspan y="199">Harbor Line</tspan><tspan x="92" y="224">Boat Academy</tspan></text>
      </g>

      <g class="identity">
        <text class="person-name" x="384" y="100">DANA R. HOLLOWAY</text>
        <text class="person-role" x="384" y="130">USCG Licensed Captain</text>
        <text class="person-role" x="384" y="156">Certified Instructor</text>
      </g>

      <g class="text-line">
        <rect x="384" y="208" width="268" height="38" rx="19" fill="var(--crimson)"/>
        <text class="pill-label" x="402" y="234">TEXT</text>
        <g class="icon-phone" transform="translate(460 217)">
          <rect width="20" height="20" rx="5" fill="var(--white)"/>
          <path d="M6 5 l3 0 l1 3 l-2 1.5 a7 7 0 0 0 3.5 3.5 l1.5 -2 l3 1 l0 3 a2 2 0 0 1 -2 1.5 a11 11 0 0 1 -10 -10 a2 2 0 0 1 1.5 -2z" fill="var(--crimson)"/>
        </g>
        <text class="pill-phone" x="490" y="234">(555) 304-8826</text>
      </g>

      <g class="contact-list">
        <g class="icon-mail" transform="translate(392 272)">
          <rect width="18" height="16" rx="3" fill="var(--gold)"/>
          <path d="M4 5 h10 v7 h-10z M4 5 l5 4 l5 -4" fill="none" stroke="var(--black)" stroke-width="1.3"/>
        </g>
        <text class="contact-line" x="420" y="285">hello@helmready.com</text>
        <g class="icon-web" transform="translate(392 300)">
          <rect width="18" height="16" rx="3" fill="var(--gold)"/>
          <circle cx="9" cy="8" r="5" fill="none" stroke="var(--black)" stroke-width="1.3"/>
          <path d="M4 8 h10 M9 3 v10" stroke="var(--black)" stroke-width="1"/>
        </g>
        <text class="contact-line" x="420" y="313">www.HelmReady.com</text>
      </g>
    </g>
  </g>
</svg>
</body>
</html>
```